Global lighting company needs compelling e-tail graphic

Our company is a global lighting company that sells light bulbs, lighting fixtures and ceiling fans. For this project, we have a concept developed for a graphic that explains color temperature for LED light bulbs. We would like to develop this concept into something more exciting and polished for consumer-friendly use on our e-tail product pages.Color temperature, in simple terms, is the ambience and atmosphere created by the color of a light bulb. More detailed information about color temperature can be found here: http://www.brantmoorlamps.com/color-temperature.aspx

Target Market(s)

Online consumers, homeowners

Industry/Entity Type

Lighting Fixture

Font styles to use
Sans Serif

Colors

Designer to choose colors to be used in the design.

Requirements
Must have
• Images depicting color temperature, preferably residential room scenes

```html
<!DOCTYPE html>
<html lang="en">
<head>
<meta charset="utf-8">
<title>Color Temperature Guide</title>
<link href="https://fonts.googleapis.com/css2?family=Montserrat:wght@400;800;900&display=swap" rel="stylesheet">
<style>
  :root {
    --canvas: #ffffff;
    --panel: #f2f2f2;
    --ink: #111111;
    --label-ink: #1c1c1c;
    --warm: #ff3d00;
    --amber: #f9a23a;
    --yellow: #fff04e;
    --cream: #fffbe6;
    --white: #ffffff;
    --sky: #1ed0ff;
  }
  * { margin: 0; padding: 0; box-sizing: border-box; }
  html, body {
    width: 1200px; height: 686px; overflow: hidden;
    background: var(--canvas);
    font-family: "Montserrat", Arial, sans-serif;
  }
  .guide { position: relative; width: 1200px; height: 686px; }
  .guide-header {
    position: absolute; left: 62px; top: 98px; width: 1058px; height: 78px;
    background: linear-gradient(90deg, var(--warm) 0%, var(--amber) 16%, var(--yellow) 32%, var(--cream) 62%, var(--white) 74%, var(--sky) 100%);
    display: flex; align-items: center; justify-content: center;
  }
  .guide-title {
    font-weight: 900; font-size: 26.5px; letter-spacing: 0.2px;
    color: var(--ink); text-transform: uppercase; white-space: nowrap;
    padding-top: 2px;
  }
  .temp-card {
    position: absolute; top: 176px; width: 345px; height: 448px;
    background: var(--panel);
    border-radius: 0 0 70px 70px / 0 0 60px 60px;
  }
  .temp-card--warm { left: 62px; }
  .temp-card--neutral { left: 418px; }
  .temp-card--cool { left: 775px; }
  .room-photo {
    position: absolute; left: 0; top: 26px; width: 345px; height: 230px;
  }
  .room-photo--warm { background: radial-gradient(ellipse at 65% 25%, #f6c77a 0%, #9a7b62 35%, #5a5048 70%, #3a3330 100%); }
  .room-photo--neutral { background: radial-gradient(ellipse at 65% 25%, #f4ecd6 0%, #8d8e92 35%, #5c6068 70%, #3c4048 100%); }
  .room-photo--cool { background: radial-gradient(ellipse at 65% 25%, #f3efe2 0%, #6f7c90 35%, #4c5a70 70%, #2c3850 100%); }
  .mood-label {
    position: absolute; left: 0; top: 455px; width: 100%;
    text-align: center; font-weight: 400; font-size: 27px; letter-spacing: 0.5px;
    color: var(--label-ink); text-transform: uppercase; white-space: nowrap;
  }
  .kelvin-tab {
    position: absolute; left: 25px; top: 342px; width: 295px; height: 92px;
    border-radius: 0 0 148px 148px / 0 0 80px 80px;
    display: flex; align-items: center; justify-content: center;
    font-weight: 900; font-size: 26px; color: var(--ink);
    padding-bottom: 4px;
  }
  .mood-label { top: 278px; }
  .kelvin-tab--warm { background: linear-gradient(90deg, var(--warm) 0%, var(--amber) 60%, #ffe14a 100%); }
  .kelvin-tab--neutral { background: linear-gradient(90deg, #fff04e 0%, #fdf6b8 50%, #fffdf2 100%); }
  .kelvin-tab--cool { background: linear-gradient(90deg, #ffffff 0%, #c6f2ff 45%, var(--sky) 100%); }
</style>
</head>
<body>
<main class="guide">
  <header class="guide-header">
    <h1 class="guide-title">Color temperature affects the mood and ambience of a room</h1>
  </header>

  <section class="temp-card temp-card--warm">
    <div class="room-photo room-photo--warm" role="img" aria-label="Table lamp, potted plant and moon lamp lit by warm amber light"></div>
    <p class="mood-label">Cozy, Calm, Inviting</p>
    <div class="kelvin-tab kelvin-tab--warm">2700K - 3000K</div>
  </section>

  <section class="temp-card temp-card--neutral">
    <div class="room-photo room-photo--neutral" role="img" aria-label="Table lamp, potted plant and moon lamp lit by neutral white light"></div>
    <p class="mood-label">Bright, Vibrant</p>
    <div class="kelvin-tab kelvin-tab--neutral">4000K</div>
  </section>

  <section class="temp-card temp-card--cool">
    <div class="room-photo room-photo--cool" role="img" aria-label="Table lamp, potted plant and moon lamp lit by cool bluish daylight"></div>
    <p class="mood-label">Crisp, Invigorating</p>
    <div class="kelvin-tab kelvin-tab--cool">5000K</div>
  </section>
</main>
</body>
</html>
```